K7 clearline

We are a glazing company specializing in frameless glass .
I would like the business cards in black with the logo taking up the most part of the front added with " frameless glass specialist's " below it.
On the back side I would like a list of what we do :
• shower screens
• glass balustrade / pool fencing
• mirrors
•office partitions
• sky lights
•shop fronts
•splash backs
Also include this information :
📧 - marcus@k7clearline.com
📞Marcus - 0412967528
📞 Colin - 0457 213 684
Updates
To all designs already posted can you include on the back of the card in the services part -
•splash backs
Target Market(s)
High end builders
Industry/Entity Type
Glazing
Contact Information for Business Card
On the back side I would like a list of what we do : • shower screens • glass balustrade / pool fencing • mirrors •office partitions • sky lights •shop fronts Also include this information : 📧 - marcus@k7clearline.com 📞Marcus - 0412967528 📞 Colin - 0457 213 684
Colors
Designer to choose colors to be used in the design.
Look and feel
Each slider illustrates characteristics of the customer's brand and the style your logo design should communicate.

```html
<!DOCTYPE html>
<html lang="en">
<head>
<meta charset="utf-8">
<title>K7 clearline – Business Card</title>
<link rel="stylesheet" href="https://fonts.googleapis.com/css2?family=Montserrat:wght@400;700&family=Roboto:wght@400;700&display=swap">
<style>
  :root {
    --page: #f1f1f1;
    --card: #000000;
    --white: #ffffff;
    --mint: #5cc791;
    --teal: #1fb3a8;
    --ocean: #0c8fb0;
    --accent: #2ab5a2;
  }
  * { margin: 0; padding: 0; box-sizing: border-box; }
  html, body { width: 1200px; height: 1200px; overflow: hidden; background: var(--page); }
  .card {
    position: absolute;
    left: 203px;
    width: 794px;
    height: 453px;
    background: var(--card);
    border-radius: 44px;
    overflow: hidden;
  }
  .card--front { top: 101px; }
  .card--back { top: 644px; }

  /* Front */
  .rule {
    position: absolute;
    top: 328px;
    height: 11px;
    background: linear-gradient(90deg, var(--mint), var(--teal) 55%, var(--ocean));
  }
  .rule--left { left: 0; width: 171px; }
  .rule--right { left: 622px; right: 0; }
  .brand-name {
    position: absolute;
    left: 0; right: 0;
    top: 206px;
    text-align: center;
    font-family: "Montserrat", sans-serif;
    font-weight: 700;
    font-size: 56px;
    letter-spacing: 1px;
    color: var(--white);
  }
  .tagline {
    position: absolute;
    left: 0; right: 0;
    top: 356px;
    text-align: center;
    font-family: "Montserrat", sans-serif;
    font-weight: 400;
    font-size: 19px;
    letter-spacing: 1.6px;
    color: var(--white);
  }

  /* Back */
  .contact {
    position: absolute;
    left: 52px;
    font-family: "Roboto", sans-serif;
    font-weight: 700;
    color: var(--white);
  }
  .contact__name { margin-left: 28px; font-size: 28px; line-height: 36px; }
  .contact__phone { display: flex; align-items: center; gap: 8px; font-size: 28px; line-height: 36px; }
  .contact__phone svg { width: 20px; height: 22px; }
  .contact--first { top: 141px; }
  .contact--second { top: 238px; }

  .divider {
    position: absolute;
    left: 393px;
    top: 84px;
    width: 7px;
    height: 287px;
    background: var(--accent);
  }
  .services {
    position: absolute;
    left: 424px;
    top: 90px;
    list-style: none;
    font-family: "Roboto", sans-serif;
    font-weight: 400;
    font-size: 28px;
    line-height: 34.2px;
    color: var(--accent);
  }
  .services li { position: relative; padding-left: 16px; }
  .services li::before {
    content: "";
    position: absolute;
    left: 0; top: 14px;
    width: 5px; height: 5px;
    background: var(--accent);
  }
  .services .continuation { padding-left: 20px; }
  .services .continuation::before { display: none; }

  .email {
    position: absolute;
    left: 216px;
    top: 408px;
    display: flex;
    align-items: center;
    gap: 22px;
    font-family: "Montserrat", sans-serif;
    font-weight: 400;
    font-size: 19px;
    color: var(--white);
  }
  .email svg { width: 31px; height: 20px; }
</style>
</head>
<body>
  <section class="card card--front">
    <div class="rule rule--left"></div>
    <div class="rule rule--right"></div>
    <h1 class="brand-name">K7 clearline</h1>
    <p class="tagline">FRAMELESS GLASS SPECIALIST'S</p>
  </section>

  <section class="card card--back">
    <div class="contact contact--first">
      <p class="contact__name">MARCUS</p>
      <p class="contact__phone">
        <svg viewBox="0 0 20 22" aria-hidden="true"><path d="M5 1 L8 6 L6 8.5 C7 11.5 9 14 12 15.5 L14.5 13.5 L19 16.5 L17 20.5 C9 21 1 12 1 4 Z" fill="var(--accent)"/></svg>
        0412967528
      </p>
    </div>
    <div class="contact contact--second">
      <p class="contact__name">COLIN</p>
      <p class="contact__phone">
        <svg viewBox="0 0 20 22" aria-hidden="true"><path d="M5 1 L8 6 L6 8.5 C7 11.5 9 14 12 15.5 L14.5 13.5 L19 16.5 L17 20.5 C9 21 1 12 1 4 Z" fill="var(--accent)"/></svg>
        0457 213 684
      </p>
    </div>

    <div class="divider"></div>

    <ul class="services">
      <li>SHOWER SCREENS</li>
      <li>GLASS BALUSTRADE /</li>
      <li class="continuation">POOL FENCING</li>
      <li>MIRRORS</li>
      <li>OFFICE PARTITIONS</li>
      <li>SKY LIGHTS</li>
      <li>SHOP FRONTS</li>
      <li>SPLASH BACKS</li>
    </ul>

    <p class="email">
      <svg viewBox="0 0 31 20" aria-hidden="true">
        <rect x="0" y="0" width="31" height="20" fill="var(--accent)"/>
        <path d="M1 1 L15.5 12 L30 1 M1 19 L12 9 M30 19 L19 9" stroke="var(--card)" stroke-width="1.6" fill="none"/>
      </svg>
      marcus@k7clearline.com
    </p>
  </section>
</body>
</html>
```